Case Management business card

Catastrophic Case Management
I'm looking for a design that best fits the words Bellwood and Catastrophic.
We need a business card for a new business based in Michigan Called Bellwood Restorative Care Coordination Group, LLC.
We provide services to clients who have been injured in a car accident and requires assistance of a case manager to facilitate and collaborate care services with or for them to help them on the road from injury to recovery. We would like to use the colors green and orange. The final design should communicate health maintenance and recovery.
We offer an comprehensive head to toe assessment.
We facilitate collaboration with your personalized injury care team members.
We assist with home and attendant care services.
We have a Team of Case managers who's main focus is continuity of care and recovery from motor vehicle injuries.

Industry/Entity Type

Business

Contact Information for Business Card

Bellwood Restorative Care Coordination Group, LLC
Catastrophic and Medical Case Management Services
2873 N. Carlow # 504318
Ypsilanti Michigan 48352
Lorna Vance RN, CM
Director of Case Management
lvance@bellwoodrccg.com
Ph: 734-518-4937
Fax: 734-518-4071

```html
<!DOCTYPE html>
<html lang="en">
<head>
<meta charset="utf-8">
<title>Bellwood Restorative Care Coordination Group – Business Card</title>
<link rel="stylesheet" href="https://fonts.googleapis.com/css2?family=Arimo:wght@400;700&display=swap">
<style>
  :root {
    --card-white: #ffffff;
    --ink: #111111;
    --shadow-black: #0b0b0b;
    --slate-grey: #353535;
    --accent-green: #33ff00;
    --accent-orange: #ff8000;
  }
  html, body {
    margin: 0;
    padding: 0;
    overflow: hidden;
    background: var(--card-white);
  }
  .card {
    position: relative;
    width: 1200px;
    height: 774px;
    overflow: hidden;
    background: var(--card-white);
    font-family: "Arimo", Arial, sans-serif;
    color: var(--ink);
  }
  .card__backdrop {
    position: absolute;
    inset: 0;
    width: 1200px;
    height: 774px;
  }
  .card__title {
    position: absolute;
    left: 774px;
    top: 293px;
    transform: translate(-50%, -50%);
    margin: 0;
    font-size: 46px;
    font-weight: 700;
    white-space: nowrap;
    letter-spacing: -0.2px;
  }
  .contact {
    position: absolute;
    margin: 0;
    font-size: 41px;
    font-weight: 400;
    white-space: nowrap;
  }
  .contact--email {
    right: 150px;
    top: 374px;
    transform: translateY(-50%);
  }
  .contact--phone {
    left: 774px;
    top: 465px;
    transform: translate(-50%, -50%);
  }
  .contact-icon {
    position: absolute;
    width: 74px;
    height: 74px;
  }
  .contact-icon--web { left: 1084px; top: 335px; }
  .contact-icon--phone { left: 1084px; top: 427px; }
</style>
</head>
<body>
<main class="card">
  <svg class="card__backdrop" viewBox="0 0 1000 635" preserveAspectRatio="none" aria-hidden="true">
    <!-- top chevrons -->
    <polygon points="0,0 62,0 130,68 100,97" fill="var(--slate-grey)"/>
    <polygon points="62,0 200,0 115,83" fill="var(--shadow-black)"/>
    <polygon points="200,0 262,0 328,66 297,95" fill="var(--slate-grey)"/>
    <polygon points="262,0 395,0 312,80" fill="var(--shadow-black)"/>
    <!-- bottom chevrons -->
    <polygon points="193,635 290,538 387,635" fill="var(--slate-grey)"/>
    <polygon points="193,635 262,566 331,635" fill="var(--shadow-black)"/>
    <polygon points="390,635 487,535 585,635" fill="var(--slate-grey)"/>
    <polygon points="390,635 459,566 528,635" fill="var(--shadow-black)"/>
    <!-- left accent bands -->
    <polygon points="0,35 285,440 120,635 0,635" fill="var(--accent-orange)"/>
    <polygon points="0,78 262,440 104,635 0,635" fill="var(--card-white)"/>
    <polygon points="0,102 238,440 90,635 0,635" fill="var(--accent-green)"/>
  </svg>

  <h1 class="card__title">Director of Case Management</h1>
  <p class="contact contact--email">lvance@bellwoodrccg.com</p>
  <p class="contact contact--phone">Ph: 734-518-4937</p>

  <svg class="contact-icon contact-icon--web" viewBox="0 0 64 64" aria-hidden="true">
    <circle cx="32" cy="32" r="30" fill="var(--accent-green)" stroke="var(--shadow-black)" stroke-width="1.5"/>
    <g fill="none" stroke="var(--card-white)" stroke-width="2.4">
      <circle cx="32" cy="32" r="18"/>
      <ellipse cx="32" cy="32" rx="8" ry="18"/>
      <line x1="32" y1="14" x2="32" y2="50"/>
      <line x1="14" y1="32" x2="50" y2="32"/>
      <line x1="17" y1="23" x2="47" y2="23"/>
      <line x1="17" y1="41" x2="47" y2="41"/>
    </g>
  </svg>

  <svg class="contact-icon contact-icon--phone" viewBox="0 0 64 64" aria-hidden="true">
    <circle cx="32" cy="32" r="29" fill="var(--card-white)" stroke="var(--accent-green)" stroke-width="3.5"/>
    <path d="M13 27 C 16 19, 48 19, 51 27 L 50 31 L 42 30 L 41 26 C 36 24, 28 24, 23 26 L 22 30 L 14 31 Z" fill="var(--ink)"/>
    <path d="M23 32 L 41 32 L 47 44 L 17 44 Z" fill="var(--ink)"/>
    <circle cx="32" cy="38" r="3.6" fill="var(--card-white)"/>
  </svg>
</main>
</body>
</html>
```